Restaurant website built on Plinko’s responsive platform- No coding skills needed

We are looking to add to our company's website www.plinkoweb.example a new inspiration page that will include examples of sites built using Plinko's platform.
In order to make it relevant, we would like to have multiple choices for every category, one of the categories is “restaurants.”

REQUIREMENTS:
o Build a "fake" restaurant site on Plinko’s responsive platform, no real restaurant information is needed. The site will include:
1. Homepage
• Restaurant header (no logo)
• Paragraph about the restaurant (can be Lorem ipsum)
• Contact details and contact buttons
• Gribbo reviews
• Reserve-a-table widget
• Open hours
2. Menu page
• You can use any menu you'd like
• Reserve a table widget
• Photo gallery
3. Footer
• Social Media links
• Map with location of restaurant

* Order of the elements is up to the designer
* Designer may add more elements as they see fit
* Designer may alter elements from page to page
* Designer will define the site color pallet and text style

****Learn more on how to create a website on Plinko's platform here
https://clipvault.example/584736201

INSTRUCTIONS FOR THIS PROJECT:
Register for a 30-day free trial for Pro access to the platform:
http://www.plinkoweb.example/plinkopro?_dm_referral=ArtHvn

a. After registering, access the dashboard and click on “Create Responsive Website.”
b. Choose a template
c. Start editing! .
d. No need to publish. When ready, take a screenshot of the preview and submit the screenshot to this ArtHaven project. Include the URL/Link to the preview within the submission description.
e. For more information on Plinko, visit the support page at https://support.plinkoweb.example/02PlinkoOne/Quick_Guide OR call our Support line Mon.-Fri., 9AM-9PM ET.1-866-555-0147

DESIGN PREFERENCES
freestyle (not related to the Plinko brand)

DESIGN SAMPLES (for inspiration)
http://www.plinkoweb.example/responsive-website/templates

What not to include in the design -
no restrictions

DELIVERABLES:
* Website on Plinko (No PSD. No coding needed)
* Screenshot preview to ArtHaven with URL/link to your site’s preview.

ABOUT THE COMPANY:
Plinko is a website builder based in California that allow designers, web designers and practically anyone to build its own site. No development and/or technical skills required.

NOTE:
* Plinko is an external site and is not part of ArtHaven
* Please refer to Plinko's Terms and Conditions for information regarding how submissions will be handled (http://www.plinkoweb.example/legal/terms)

Target Market(s)

SMBs and web designers that want to create simple, professional and beautiful websites

Industry/Entity Type

Restaurant

Number of Pages Required

2 page

Requirements
Must have
• Please send a preview of the site you created on Plinko, NOT a PSD/JPEG
Should not have
• No coding skills are needed- any web designer can build a site on Plinko

```html
<!DOCTYPE html>
<html lang="en">
<head>
<meta charset="utf-8">
<title>Restaurant</title>
<link rel="stylesheet" href="https://fonts.googleapis.com/css2?family=Source+Sans+3:wght@300;400;600;700&family=Open+Sans:wght@400;600&family=Alfa+Slab+One&display=swap">
<style>
  :root {
    --green: #78b800;
    --green-btn: #67b033;
    --black: #000000;
    --dark: #2e2e2e;
    --text: #333333;
    --muted: #666666;
    --field: #e2e2e2;
    --coupon-border: #4fb2c7;
    --coupon-bg: #e4eef2;
    --white: #ffffff;
  }
  * { box-sizing: border-box; margin: 0; padding: 0; }
  html, body { width: 1200px; height: 3180px; overflow: hidden; }
  body { position: relative; background: var(--white); color: var(--text); font-family: "Open Sans", sans-serif; }
  .abs { position: absolute; }

  /* hero */
  .hero { left: 0; top: 0; width: 1200px; height: 583px;
    background: linear-gradient(100deg, #f4f4f2 0%, #e8e6e2 35%, #d9cfc0 60%, #c99a5a 80%, #b85d2c 100%); }
  .topbar { left: 0; top: 0; width: 1200px; height: 55px;
    background: repeating-linear-gradient(135deg, #1a1a1a 0 3px, #262626 3px 6px); }
  .brand { left: 153px; top: 8px; color: var(--white); font: 400 32px/40px "Source Sans 3", sans-serif; }
  .social { right: 116px; top: 19px; display: flex; gap: 12px; }
  .social span { width: 16px; height: 16px; border-radius: 50%; background: var(--white); display: block; }
  .hero-title { left: 0; width: 1200px; top: 170px; text-align: center; font: 400 62px/80px "Source Sans 3", sans-serif; color: var(--black); }
  .hero-text { left: 170px; width: 860px; top: 264px; text-align: center; font: 400 20px/32px "Open Sans", sans-serif; color: var(--black); }
  .btn-dark { left: 490px; top: 365px; width: 222px; height: 44px; background: var(--black); color: var(--white);
    font: 400 19px/44px "Open Sans", sans-serif; padding-left: 80px; }
  .btn-dark svg { position: absolute; left: 12px; top: 11px; }

  /* nav */
  .nav { left: 0; top: 583px; width: 1200px; height: 64px; background: var(--green); display: flex; justify-content: center; align-items: center; gap: 50px; padding-left: 130px; }
  .nav a { color: var(--white); text-decoration: none; font: 600 17px "Source Sans 3", sans-serif; text-transform: uppercase; }
  .nav a.plain { text-transform: none; }
  .nav a.current { color: #dff0b8; }

  /* about */
  .about-title { left: 0; width: 1200px; top: 698px; text-align: center; font: 300 48px/62px "Source Sans 3", sans-serif; color: #333; }
  .about-title strong { font-weight: 600; }
  .about-sub { left: 0; width: 1200px; top: 772px; text-align: center; font: 400 24px/32px "Source Sans 3", sans-serif; color: #333; }
  .about-text { left: 178px; width: 954px; top: 828px; text-align: center; font: 400 14.5px/24px "Open Sans", sans-serif; color: var(--muted); }
  .btn-green { background: var(--green-btn); color: var(--white); text-align: center; border-radius: 3px; }
  .find-table { left: 515px; top: 918px; width: 280px; height: 53px; font: 400 22px/53px "Source Sans 3", sans-serif; }

  /* bands */
  .band { left: 0; width: 1200px; text-align: center; color: var(--white); font: 400 42px "Source Sans 3", sans-serif; }
  .band strong { font-weight: 700; }
  .band-gallery { top: 1041px; height: 72px; line-height: 72px; background: var(--black); }
  .band-here { top: 1514px; height: 76px; line-height: 76px; background: var(--black); }
  .band-others { top: 2001px; height: 70px; line-height: 70px; background: var(--green); font-weight: 600; }

  .gallery { left: 0; top: 1113px; width: 1200px; height: 401px; display: flex; }
  .gallery div { flex: 1; }
  .g1 { background: linear-gradient(135deg, #e8e4dc, #a89a80 60%, #5a4030); }
  .g2 { background: linear-gradient(160deg, #6a4a2c, #d8b860 50%, #8a6a40); }
  .g3 { background: linear-gradient(150deg, #f0e8dc, #8a4a24 50%, #4a2410); }

  .map { left: 0; top: 1590px; width: 1200px; height: 411px; background: linear-gradient(120deg, #cfe3f0, #e8e4d8 40%, #e6e2d4 70%, #c8dced); }

  /* testimonial */
  .avatar { left: 295px; top: 2131px; width: 174px; height: 174px; border-radius: 50%; background: linear-gradient(160deg, #c8a890, #8a6450); border: 5px solid #f0f0f0; box-shadow: 0 0 0 1px #ddd; }
  .quote { left: 174px; top: 2326px; width: 480px; font: 400 12.5px/21px "Open Sans", sans-serif; color: #444; white-space: nowrap; }
  .author { left: 174px; top: 2505px; font: 600 14px/18px "Open Sans", sans-serif; color: var(--green); }
  .date { left: 403px; top: 2507px; font: 400 12px/16px "Open Sans", sans-serif; color: #333; }

  /* coupon */
  .coupon { left: 615px; top: 2133px; width: 415px; height: 360px; border: 2px solid var(--coupon-border); }
  .coupon h3 { position: absolute; left: 11px; top: 12px; font: 400 43px/50px "Source Sans 3", sans-serif; color: #222; }
  .coupon-body { position: absolute; left: 11px; top: 83px; width: 390px; height: 172px; background: var(--coupon-bg); }
  .coupon-body p { position: absolute; left: 12px; width: 230px; font: 400 12.5px/17px "Open Sans", sans-serif; color: #555; }
  .offer { position: absolute; right: 0; top: 0; width: 143px; height: 172px; background: var(--black); color: var(--white);
    font: 400 52px/60px "Alfa Slab One", serif; padding: 16px 0 0 12px; border-left: 4px dashed var(--white); }
  .use-coupon { position: absolute; left: 11px; top: 265px; width: 390px; height: 37px; background: var(--green); color: var(--white);
    font: 600 14px/37px "Open Sans", sans-serif; padding-left: 8px; }
  .shares { position: absolute; left: 11px; top: 313px; display: flex; gap: 6px; }
  .shares span { height: 27px; border: 1px solid #ccc; background: #f6f6f6; font: 400 11px/25px "Open Sans", sans-serif; color: #555; padding: 0 8px 0 5px; display: flex; align-items: center; gap: 5px; }
  .shares i { width: 14px; height: 14px; display: block; background: #777; }

  .divider { left: 100px; top: 2586px; width: 990px; height: 2px; background: #999; }

  /* contact */
  .contact-title { left: 123px; top: 2627px; font: 400 47px/60px "Source Sans 3", sans-serif; color: #111; }
  .label { font: 400 14px "Open Sans", sans-serif; color: #333; }
  .field { height: 38px; background: var(--field); border: 1px solid #d6d6d6; }
  .send { left: 787px; top: 2934px; width: 279px; height: 47px; font: 400 18px/47px "Open Sans", sans-serif; }

  /* footer */
  .footer { left: 0; top: 3078px; width: 1200px; height: 102px; background: var(--dark); color: var(--white); text-align: center; }
  .footer nav { position: absolute; left: 0; top: 32px; width: 1200px; display: flex; justify-content: center; gap: 40px; }
  .footer nav a { color: var(--white); text-decoration: none; font: 400 14px "Open Sans", sans-serif; }
  .copyright { position: absolute; left: 0; top: 60px; width: 1200px; font: 400 14px "Open Sans", sans-serif; }
  .copyright em { font-style: normal; color: var(--green); }
</style>
</head>
<body>
  <header>
    <div class="abs hero" role="img" aria-label="Photo of a dressed dinner table with wine glasses and plated seafood dishes"></div>
    <div class="abs topbar"></div>
    <div class="abs brand">Restaurant</div>
    <div class="abs social" aria-label="Social links"><span></span><span></span><span></span></div>
    <h1 class="abs hero-title">Unique &amp; Delicious Taste</h1>
    <p class="abs hero-text">Lorem ipsum dolor sit amet, consectetur adipiscing elit. Phasellus lobortis dictum elit eu placerat. Nullam velpellentesque tortor .</p>
    <div class="abs btn-dark">
      <svg width="24" height="22" viewBox="0 0 24 22" fill="#fff"><rect x="2" y="0" width="2" height="8"/><rect x="6" y="0" width="2" height="8"/><rect x="2" y="6" width="6" height="4"/><rect x="4" y="8" width="2.5" height="14"/><path d="M15 0c3 0 4 4 4 9h-2v13h-2.5z"/></svg>
      Read More
    </div>
    <nav class="abs nav">
      <a href="#">Welcome</a><a href="#">Our Stories</a><a href="#">Our Photos</a><a href="#">We Were Here</a><a class="current" href="#">By Me</a><a class="plain" href="#">Home</a>
    </nav>
  </header>

  <section class="about">
    <h2 class="abs about-title">About Our <strong>Restaurant</strong></h2>
    <p class="abs about-sub">This is a paragraph. Writing in paragraphs lets your visitor</p>
    <p class="abs about-text">This is a paragraph. Writing in paragraphs lets your visitor find what they are looking for quickly and easily. Make sure your titles stand out from the rest of the text.This is a paragraph. Writing in paragraphs lets your visitor find what they are looking for quickly and easily. Make sure your titles stand out from the rest of the text.</p>
    <div class="abs btn-green find-table">Find a Table</div>
  </section>

  <section class="gallery-section">
    <h2 class="abs band band-gallery">OUR<strong>#Gallery</strong></h2>
    <div class="abs gallery">
      <div class="g1" role="img" aria-label="Waiter carrying plated dishes in the dining room"></div>
      <div class="g2" role="img" aria-label="Bowl of pasta with herbs and olive oil"></div>
      <div class="g3" role="img" aria-label="Glazed bundt cake"></div>
    </div>
  </section>

  <section class="location">
    <h2 class="abs band band-here">WE<strong>WERE HERE</strong></h2>
    <div class="abs map" role="img" aria-label="Street map showing the restaurant location"></div>
  </section>

  <section class="others">
    <h2 class="abs band band-others">Others</h2>
    <div class="abs avatar" role="img" aria-label="Portrait of a guest reviewer"></div>
    <p class="abs quote">This is a paragraph. Writing in paragraphs lets your visitor find what<br>they are looking for quickly and easily. Make sure your titles stand out<br>from the rest of the text. This is a paragraph. Writing in paragraphs<br>lets your visitor find what they are looking for quickly and easily.<br>Make sure your titles stand out from the rest of the text.<br>This is a paragraph. Writing in paragraphs lets your visitor find what<br>they are looking for quickly and easily. Make sure your titles stand out<br>from the rest of the text.</p>
    <div class="abs author">Ms Mira Calden</div>
    <div class="abs date">10 March 2015 Tuesday</div>

    <div class="abs coupon">
      <h3>Get A Coupon!</h3>
      <div class="coupon-body">
        <p style="top:10px">In here you should write the offer details. Example: get a $5 off on your next lunch order</p>
        <p style="top:92px">Offer available only on lunch menu items. Offer expires Dec 29th. Not valid for drinks or special dishes.</p>
        <div class="offer">$5<br>OFF</div>
      </div>
      <div class="use-coupon">Click to use coupon</div>
      <div class="shares"><span><i></i>Share</span><span><i></i>Tweet</span><span><i></i>Share</span><span><i></i>Share</span><span><i></i>Mail</span></div>
    </div>
  </section>

  <div class="abs divider"></div>

  <section class="contact">
    <h2 class="abs contact-title">Contact Us</h2>
    <div class="abs label" style="left:138px;top:2734px">Name:</div>
    <div class="abs label" style="left:456px;top:2734px">Email:</div>
    <div class="abs label" style="left:776px;top:2734px">Phone:</div>
    <div class="abs field" style="left:138px;top:2756px;width:286px"></div>
    <div class="abs field" style="left:456px;top:2756px;width:286px"></div>
    <div class="abs field" style="left:776px;top:2756px;width:288px"></div>
    <div class="abs label" style="left:138px;top:2810px">Message:</div>
    <div class="abs field" style="left:138px;top:2832px;width:926px;height:77px"></div>
    <div class="abs btn-green send">Send Message</div>
  </section>

  <footer class="abs footer">
    <nav><a href="#">Home</a><a href="#">About us</a><a href="#">Menu</a><a href="#">Gallery</a><a href="#">Services</a><a href="#">Contact us</a></nav>
    <p class="copyright">Copyright 2015 <em>Restaurant</em> . All Rights Reserved</p>
  </footer>
</body>
</html>
```